financial company web page

We are tax and financial consulting company that needs a web site. Our logo is attached. Headquarters of our company is based in Latvia, Riga. Our actual temporary web site is www.corvanteq.com The main purpose of our new web site is:
* to explain the benefits of doing business through Latvian LLC companies;
* provide necessary information about taxation regime in Latvia for trading and holding companies
* propose some standard schemes of using Latvian companies for various businesses.
* offer our clients other jurisdictions companies - other European, offshore, etc.
* offer our clients ecommerce solutions
* offer our client residency in Latvia and EU
Registration of a Latvian company + accounting + legal advice will be our primary product. However, web site first page should highlight 4 other important products, such as:
1 - eCommerce (here we will explain briefly what is eCommerce, how our client can use it, what are the bonuses doing business online, explain conditions of eCommerce, etc) ;
2 - Residence Permit (here we offer EU and non-EU citizens to obtain Latvian residence permit and explain the benefits of having Latvian ID card);
3 - other Jurisdictions (here we propose list of other companies registered in the countries with favorable taxation regime, i.e. UK, Hong-Kong, Canada, Panama, BVI, UAE, etc);
4 - banking (here we explain benefits of having bank account in Latvia, explaining briefly products that bank offer, etc).
Overall Website map is the following:
1. About us
2. About Latvia
3. Contacts
4. Latvian company
5. Our services
a. еCommerce
b. Resident permit (Latvia and EU)
c. Bank accounts
d. Registration and support of other jurisdictions (European companies, Low tax companies, Offshore companies)
e. Additional services (Tax advisory, Virtual office, European licenses, Accounting services, Legal address in Riga)
6. Become Partner
7. Corvanteq Travel Guide
As a start point we need only first page design. If this design suits us well we will continue to work with you on other pages. We are looking for innovative, creative and professional design in line with our corporate logo and colours. We want this design to focus more on graphic, on simplicity and usability. It should be immediately clear from the first glance what the site is about, what is our key product and how to get more information if I'm interested on something.
These are website from our sector, we want to be better:
http://www.marlowbayholdings.com/
http://www.qtr-harbourline.com/
http://www.dwpenterprisehub.com/
http://www.firmsetupnorth59.co.uk/
In case you can't find our logo, please, ask I will send it to your mail. Thanks!
Target Market(s)
European, Russian or Chinesee enterpreneurs
Industry/Entity Type
Accounting
Requirements
Must have
- Web site will be on 10 languages, so somewhere must be a button/flag to switch language.
Contact information should be on every page (phone number and add Chatterloop buttons or similar).
Search button should be available on the first page
Button Request a Call should be on every page.
Visitors should also have a possibility to download a brochure about each product (so appropriate button should be in each section).

```html
<!DOCTYPE html>
<html lang="en">
<head>
<meta charset="utf-8">
<title>Corvanteq – Tax and Financial Solutions</title>
<link rel="stylesheet" href="https://fonts.googleapis.com/css2?family=Open+Sans:wght@400;600;700&display=swap">
<style>
:root{
  --navy:#24386c;
  --navy-deep:#1b2b58;
  --navy-menu:#22356a;
  --menu-active:#14214a;
  --accent:#3a8fd0;
  --link:#2f8fd2;
  --text:#4a4a4a;
  --muted:#8a8f99;
  --panel:rgba(78,96,150,.78);
  --white:#ffffff;
  --line:#dcdfe5;
}
*{box-sizing:border-box;margin:0;padding:0}
html,body{width:1200px;height:645px;overflow:hidden;background:var(--white);font-family:"Open Sans",Arial,sans-serif;color:var(--text)}
.page{position:relative;width:1200px;height:645px;overflow:hidden}
.abs{position:absolute}

/* header */
.brand{left:24px;top:18px;display:flex;align-items:center;gap:10px}
.brand-mark{width:26px;height:26px;background:var(--navy)}
.brand-name{font-size:32px;font-weight:700;color:var(--navy);letter-spacing:-.3px}
.top-links{right:224px;top:29px;display:flex;align-items:center;font-size:11px;color:#444;white-space:nowrap}
.top-links .sep{width:1px;height:12px;background:var(--line);margin:0 9px}
.flag{width:13px;height:9px;margin-left:10px;background:linear-gradient(#9e3039 0 40%,#fff 40% 60%,#9e3039 60%)}
.search{left:1001px;top:23px;width:173px;height:27px;border:1px solid var(--line)}
.search svg{position:absolute;right:8px;top:8px}

/* nav */
.nav{left:0;top:75px;width:1200px;height:35px;background:var(--navy)}
.nav-item{position:absolute;top:0;height:35px;line-height:35px;font-size:13.5px;color:#c9d2e8;white-space:nowrap}
.nav-item.is-active{background:var(--navy-menu);color:var(--white);font-weight:600;width:148px;text-align:center}
.request-call{position:absolute;left:1076px;top:6px;width:99px;height:23px;background:var(--accent);color:#fff;font-size:10px;font-weight:600;text-align:center;line-height:23px;letter-spacing:.2px}

/* hero */
.hero{left:0;top:110px;width:1200px;height:402px;background:linear-gradient(180deg,#b9cce4 0%,#d6e0ec 28%,#c4cdd8 40%,#8f97a3 55%,#6d6f79 75%,#5a5a62 100%)}
.dropdown{left:138px;top:110px;width:148px;height:151px;background:var(--navy-menu);padding-top:8px}
.dropdown a{display:block;height:33.5px;line-height:33.5px;padding-left:16px;font-size:11.5px;color:#c9d2e8;text-decoration:none}
.dropdown a.is-active{background:var(--menu-active);color:#fff}

.panel{left:24px;top:283px;width:1151px;height:199px;background:var(--panel)}
.service{position:absolute;width:100px;text-align:center;color:#fff;font-size:11.5px;font-weight:600;line-height:13px}
.service svg{display:block;margin:0 auto 8px}
.grid-line{position:absolute;background:rgba(255,255,255,.35)}
.why-title{left:369px;top:21px;font-size:16px;font-weight:600;color:#fff}
.why-thumb{left:371px;top:56px;width:115px;height:83px;border:2px solid #fff;background:linear-gradient(135deg,#c9b6a0,#8a7a6c 55%,#5b6b80)}
.why-text{left:509px;top:55px;width:615px;font-size:11.2px;line-height:15.4px;color:#f1f3f8}
.view-more{left:1047px;top:152px;width:77px;height:22px;background:var(--navy-deep);color:#fff;font-size:11px;text-align:center;line-height:22px}
.dots{left:1106px;top:489px;display:flex;gap:7px}
.dots span{width:12px;height:12px;border:2px solid #fff;border-radius:50%}
.dots span.is-active{background:var(--accent)}

/* news bar */
.newsbar{left:0;top:512px;width:1200px;height:43px;background:var(--navy);color:#fff;font-size:11.5px}
.newsbar .msg{position:absolute;left:24px;top:13px;display:flex;align-items:center;gap:12px}
.newsbar a{color:var(--link);text-decoration:none}
.newsbar .links{position:absolute;right:26px;top:14px;display:flex;gap:17px}

/* footer */
.footer-left{left:24px;top:586px;font-size:10px;line-height:16px;color:#555;white-space:nowrap}
.footer-left a,.footer-news a{color:var(--link);text-decoration:none}
.footer-news{left:377px;top:586px;font-size:10px;line-height:16px;color:#555;white-space:nowrap}
.footer-news b{font-weight:600}
.contact-phone{left:752px;top:585px;text-align:right;width:142px;white-space:nowrap}
.contact-phone .num{font-size:15.5px;line-height:20px;color:#666;display:flex;align-items:center;justify-content:flex-end;gap:5px}
.contact-phone .mail{font-size:10px;color:var(--muted)}
.vline{width:1px;height:30px;background:var(--line);top:586px}
.chat{left:934px;top:586px;display:flex;gap:8px;white-space:nowrap}
.chat .dot{width:15px;height:15px;border-radius:50%;background:var(--link);margin-top:2px}
.chat .name{font-size:12px;font-weight:700;color:#555;line-height:14px}
.chat .sub{font-size:10px;color:var(--muted)}
.social{left:1062px;top:592px;display:flex;gap:17px}
.social span{width:15px;height:15px;border-radius:50%;background:#c3c7cf}
</style>
</head>
<body>
<div class="page">

  <header>
    <div class="abs brand"><span class="brand-mark"></span><span class="brand-name">Corvanteq</span></div>
    <div class="abs top-links">
      <svg width="10" height="10" viewBox="0 0 10 10" style="margin-right:6px"><path d="M5 0 10 5H8.5V10H6V7H4V10H1.5V5H0Z" fill="#aab"/></svg>
      About Corvanteq<span class="sep"></span>Choose your language<span class="flag"></span>
      <svg width="10" height="6" viewBox="0 0 10 6" style="margin-left:8px"><path d="M1 1 5 5 9 1" stroke="#bbb" fill="none" stroke-width="1.3"/></svg>
    </div>
    <div class="abs search">
      <svg width="11" height="11" viewBox="0 0 11 11"><circle cx="4.5" cy="4.5" r="3.5" stroke="#bbb" stroke-width="1.4" fill="none"/><path d="M7 7 10 10" stroke="#bbb" stroke-width="1.6"/></svg>
    </div>
  </header>

  <nav class="abs nav">
    <span class="nav-item" style="left:22px">Latvian company</span>
    <span class="nav-item is-active" style="left:138px">European Company</span>
    <span class="nav-item" style="left:298px">eCommerce</span>
    <span class="nav-item" style="left:398px">Virtual office</span>
    <span class="request-call">REQUEST A CALL</span>
  </nav>

  <section class="abs hero" role="img" aria-label="Panoramic winter view over Riga with the frozen river, cable bridge and church spires"></section>

  <div class="abs dropdown">
    <a>European Trading</a>
    <a class="is-active">International Trading</a>
    <a>European Holding</a>
    <a>International Holding</a>
  </div>

  <section class="abs panel">
    <div class="grid-line" style="left:113px;top:19px;width:1px;height:188px"></div>
    <div class="grid-line" style="left:216px;top:19px;width:1px;height:188px"></div>
    <div class="grid-line" style="left:17px;top:107px;width:315px;height:1px"></div>

    <div class="service" style="left:11px;top:30px">
      <svg width="28" height="30" viewBox="0 0 28 30"><rect x="3" y="2" width="22" height="14" rx="2" fill="#fff"/><rect x="3" y="6" width="22" height="3" fill="#5b6c9e"/><path d="M9 14v10c0 3 2 5 5 5h6v-9l-4-3h-4v-3z" fill="#fff" stroke="#5b6c9e"/></svg>
      eCommerce
    </div>
    <div class="service" style="left:114px;top:30px">
      <svg width="26" height="30" viewBox="0 0 26 30"><rect x="5" y="2" width="18" height="24" fill="#fff"/><path d="M9 8h10M9 12h10M9 16h10M9 20h6" stroke="#5b6c9e" stroke-width="1.6"/><rect x="2" y="6" width="4" height="22" fill="#fff"/></svg>
      Resident Permit
    </div>
    <div class="service" style="left:219px;top:30px">
      <svg width="26" height="30" viewBox="0 0 26 30"><rect x="3" y="3" width="14" height="26" fill="#fff"/><rect x="17" y="11" width="7" height="18" fill="#fff"/><path d="M6 7h3M11 7h3M6 12h3M11 12h3M6 17h3M11 17h3M6 22h3M11 22h3" stroke="#5b6c9e" stroke-width="2"/></svg>
      Bank Accounts
    </div>
    <div class="service" style="left:11px;top:120px">
      <svg width="26" height="30" viewBox="0 0 26 30"><circle cx="13" cy="8" r="6" fill="#fff"/><path d="M1 29c0-8 5-13 12-13s12 5 12 13z" fill="#fff"/><path d="M13 16l-2 4 2 8 2-8z" fill="#5b6c9e"/></svg>
      eCommerce
    </div>
    <div class="service" style="left:114px;top:116px">
      <svg width="28" height="28" viewBox="0 0 28 28"><rect x="1" y="8" width="26" height="18" rx="1" fill="#fff"/><path d="M10 8V4h8v4" stroke="#fff" stroke-width="2.5" fill="none"/></svg>
      Additional<br>Services
    </div>
    <div class="service" style="left:219px;top:120px">
      <svg width="28" height="28" viewBox="0 0 28 28"><path d="M2 2h24v17H12l-6 6v-6H2z" fill="#fff"/><path d="M7 8h14M7 13h10" stroke="#5b6c9e" stroke-width="1.8"/></svg>
      Testimonials
    </div>

    <h2 class="abs why-title">Why Corvanteq</h2>
    <div class="abs why-thumb" role="img" aria-label="Consultant meeting a client at a desk with a computer"></div>
    <p class="abs why-text">Lorem ipsum dolor sit amet, consectetuer adipiscing elit, sed diam nonummy nibh euismod tincidunt ut laoreet dolore magna aliquam erat volutpat. Ut wisi enim ad minim veniam, quis nostrud exerci tation ullamcorper suscipit lobortis nisl ut aliquip ex ea commodo consequat. Claritas est etiam processus dynamicus, qui sequitur mutationem consuetudium lectorum. Mirum est notare quam littera gothica, quam nunc putamus parum claram, anteposuerit litterarum formas humanitatis per seacula quarta decima et quinta decima.</p>
    <span class="abs view-more">View more</span>
  </section>

  <div class="abs dots"><span class="is-active"></span><span></span><span></span><span></span></div>

  <section class="abs newsbar">
    <div class="msg">
      <svg width="15" height="15" viewBox="0 0 15 15"><path d="M2 13l1-4 8-8 3 3-8 8z" fill="#fff"/></svg>
      <span>Lorem ipsum dolor sit amet, consec nonummy nibh euismod tincidunt. &nbsp;<a>Readmore</a></span>
    </div>
    <div class="links"><span>Become a Partner</span><span>Sitemap</span></div>
  </section>

  <footer>
    <div class="abs footer-left">© 2013 <a>Corvanteq.com</a>&nbsp; Tax and financial solutions. All right reserved<br>Kalnciema street 18-2, Riga, LV-1048, Latvia</div>
    <div class="abs footer-news"><b>What's New at Corvanteq</b><br>New Services of Daugava Ridge Bank for More Convenient Account <a>Readmore</a></div>
    <div class="abs contact-phone">
      <div class="num"><svg width="12" height="12" viewBox="0 0 12 12"><path d="M2 1l2 0 1 3-1.5 1a7 7 0 0 0 3.5 3.5L8 7l3 1v2c0 1-1 1-1 1A9 9 0 0 1 1 2s0-1 1-1z" fill="#777"/></svg><span>+371 20457813</span></div>
      <div class="mail">info@corvanteq.com</div>
    </div>
    <div class="abs vline" style="left:916px"></div>
    <div class="abs chat"><span class="dot"></span><div><div class="name">corvanteq</div><div class="sub">for call inly</div></div></div>
    <div class="abs vline" style="left:1037px"></div>
    <div class="abs social" aria-label="Social links"><span></span><span></span><span></span><span></span></div>
  </footer>

</div>
</body>
</html>
```